Our brand new and excilting business, ZIPPA things, needs a fresh, vibriant and clean website that is

We need a new website designed to sell our ZIPPA things products to schools and fundraisers. We plan to have around 24 items with great images, add to cart and some really new and cool products. This site needs to be clean, fresh and funky, really clean lines, easy to navigate but look really fun and fresh

Target Market(s)

School fundraising. Kids

Industry/Entity Type

Business

Number of Pages Required

4 page

Colors
add136
fbee3d
fbed22
9bcb3c
f78f20

Requirements
Must have
• Fresh, fun and easy to navigate. Great shopping product page that has images of our products and add to cart
Nice to have
• Flashing image availibility
Should not have
• Must not be old and boring

```html
<!DOCTYPE html>
<html lang="en">
<head>
<meta charset="utf-8">
<title>ZIPPA things — Schools and Fundraisers</title>
<link href="https://fonts.googleapis.com/css2?family=Open+Sans:wght@400;600;700;800&display=swap" rel="stylesheet">
<style>
:root{
  --orange:#f78f20;
  --green:#9bcb3c;
  --lime:#add136;
  --yellow:#fbee3d;
  --header:#30342a;
  --ink:#222;
  --muted:#8a8a8a;
  --footer:#ececec;
  --bar:#1e1e1e;
  --white:#fff;
}
*{box-sizing:border-box;margin:0;padding:0}
html,body{width:798px;height:1200px;overflow:hidden}
body{font-family:"Open Sans",Arial,sans-serif;color:var(--ink);background:#f6f6f6;position:relative}
.abs{position:absolute}

/* header */
.site-header{left:0;top:0;width:798px;height:80px;background:var(--header)}
.brand{left:30px;top:22px;font-size:30px;font-weight:800;color:var(--orange);letter-spacing:-.5px;line-height:1}
.brand-dot{display:inline-block;width:10px;height:10px;border-radius:50%;background:var(--green);margin-left:6px;vertical-align:middle}
.top-links{right:66px;top:6px;display:flex;gap:34px;font-size:8px;color:#bfc3b5}
.top-contact{right:66px;top:28px;display:flex;gap:24px;font-size:10px;color:var(--white);font-weight:600;align-items:center}
.top-contact span{display:flex;align-items:center;gap:6px}
.icon-dot{width:15px;height:15px;border-radius:50%;background:var(--orange);display:inline-flex;align-items:center;justify-content:center}
.main-nav{right:66px;top:60px;display:flex;gap:32px;font-size:9px;font-weight:700;color:var(--white);letter-spacing:.3px}
.main-nav .active{color:var(--orange)}

/* hero */
.hero{left:0;top:80px;width:798px;height:340px;background:linear-gradient(100deg,#e23b8f 0%,#7b3cc9 22%,#1e9be0 45%,#3dc46b 70%,#f2c23a 88%,#e84a5f 100%)}
.slider{left:66px;top:100px;width:666px;height:300px;background:#0c0c0c;overflow:hidden}
.crowd{left:0;top:0;width:666px;height:300px;background:radial-gradient(ellipse 260px 140px at 0% 100%,rgba(70,170,80,.45),rgba(12,12,12,0) 100%)}
.slide-art{left:300px;top:20px;width:340px;height:260px;background:radial-gradient(ellipse at center,#ff3fa4 0%,#29d4f0 28%,#ffe83a 46%,#6cf04a 58%,rgba(12,12,12,0) 72%)}
.hero-title{left:50px;top:78px;color:var(--white);font-size:30px;font-weight:800;letter-spacing:.3px;line-height:1}
.hero-sub{left:50px;top:116px;color:var(--white);font-size:13px;font-weight:700;letter-spacing:.5px}
.hero-price{left:50px;top:142px;width:78px;height:78px;border-radius:50%;background:var(--orange);color:var(--white);text-align:center}
.hero-price small{display:block;font-size:10px;padding-top:13px}
.hero-price b{display:block;font-size:24px;font-weight:800;line-height:1.1}
.btn{display:inline-block;background:var(--orange);color:var(--white);font-size:8.5px;font-weight:700;padding:8px 16px;border-radius:2px;letter-spacing:.5px}
.hero-btn{left:50px;top:238px}

/* best sellers */
.section-title{left:66px;top:440px;font-size:18px;font-weight:800;color:var(--orange)}
.section-rule{left:66px;top:466px;width:48px;height:2px;background:var(--green)}
.arrows{right:66px;top:444px;display:flex;gap:5px}
.arrows span{width:15px;height:15px;border-radius:50%;border:1px solid #bbb;display:flex;align-items:center;justify-content:center}
.products{left:66px;top:480px;width:666px;display:flex;gap:14px}
.card{width:156px;background:var(--white);border:1px solid #e1e1e1}
.card-art{height:118px}
.art-1{background:radial-gradient(circle at 50% 50%,#ffe83a,#e2379a 40%,#0a0a0a 75%)}
.art-2{background:radial-gradient(circle at 50% 50%,#ff4fb4,#3a7bff 45%,#0a0a0a 78%)}
.art-3{background:radial-gradient(circle at 50% 50%,#b7ff3a,#21b8e8 45%,#0a0a0a 78%)}
.art-4{background:radial-gradient(circle at 50% 50%,#ffcc33,#ff4a3a 35%,#48e05a 55%,#0a0a0a 80%)}
.card-info{position:relative;height:60px;padding:12px 10px}
.card-name{font-size:8px;color:#555}
.card-price{font-size:8.5px;color:var(--orange);font-weight:700;margin-top:7px}
.stars{font-size:7px;color:var(--orange);margin-left:8px;font-weight:400}
.cart{position:absolute;right:10px;top:20px;width:20px;height:20px;border-radius:50%;background:var(--orange);display:flex;align-items:center;justify-content:center}

/* promo banners */
.promo{top:688px;width:326px;height:116px;overflow:hidden}
.promo-left{left:66px;background:var(--green)}
.promo-left .promo-art{left:0;top:0;width:326px;height:58px;background:linear-gradient(90deg,#1a1a1a,#3e8cd9 35%,#ffe83a 60%,#e23b8f 80%,#1a1a1a)}
.promo-left .promo-title{left:0;width:326px;top:70px;text-align:center;font-size:18px;font-weight:800;color:var(--orange)}
.promo-left .btn-white{left:133px;top:96px}
.btn-white{background:var(--white);color:var(--ink);font-size:7px;font-weight:700;padding:3px 10px}
.promo-right{left:406px;background:linear-gradient(120deg,#3a1d5e,#c23b86 45%,#2a7fd4 75%,#1b1b2e)}
.promo-right .promo-title{right:20px;top:26px;font-size:22px;font-weight:800;color:var(--white)}
.promo-right .promo-sub{right:46px;top:58px;font-size:7px;color:var(--white);font-weight:600}
.promo-right .btn-white{right:56px;top:76px}

/* features */
.features{left:66px;top:840px;width:666px;display:flex;justify-content:space-between}
.feature{display:flex;gap:10px;align-items:flex-start;width:210px}
.feature h4{font-size:8px;font-weight:700;color:#444}
.feature p{font-size:7px;color:var(--muted);margin-top:3px}

/* footer */
.site-footer{left:0;top:962px;width:798px;height:196px;background:var(--footer)}
.foot-brand{left:66px;top:994px;font-size:26px;font-weight:800;color:var(--orange);line-height:1}
.field{background:var(--white);border:1px solid #d6d6d6;font-size:7px;color:#999;padding:0 8px;display:flex;align-items:center;height:22px}
.field-name{left:66px;top:1064px;width:170px}
.field-email{left:66px;top:1094px;width:112px}
.subscribe{left:180px;top:1094px;height:22px;width:56px;background:var(--orange);color:var(--white);font-size:7px;font-weight:700;display:flex;align-items:center;justify-content:center}
.foot-col h5{font-size:10px;font-weight:600;color:#555;margin-bottom:9px}
.foot-col h5.accent{color:var(--orange);font-size:9.5px}
.foot-col li{list-style:none;font-size:7.5px;color:#777;line-height:13px}
.contact-col{left:300px;top:994px}
.contact-col li{display:flex;align-items:center;gap:6px;line-height:15px}
.socials{left:300px;top:1098px;display:flex;gap:6px}
.socials span{width:14px;height:14px;border-radius:2px;background:#d94a3a}
.socials span:nth-child(2){background:#3b5a99}
.socials span:nth-child(3){background:#3aa5dd}
.socials span:nth-child(4){background:#cf3b2e}
.support-col{left:478px;top:994px}
.account-col{left:648px;top:994px}
.bottom-bar{left:0;top:1158px;width:798px;height:42px;background:var(--bar);color:#9a9a9a;font-size:7px;display:flex;align-items:center;justify-content:center}
</style>
</head>
<body>

<header class="site-header abs">
  <div class="brand abs">ZIPPA things<span class="brand-dot"></span></div>
  <div class="top-links abs"><span>Checkout Account</span><span>My account</span><span>Cart</span></div>
  <div class="top-contact abs">
    <span><i class="icon-dot"><svg width="8" height="8" viewBox="0 0 10 10"><path d="M2 1l2 2-1 1.5c.8 1.4 1.7 2.3 3 3L7.5 6l2 2-1.5 1.5C4.5 9 1 5.5.5 2z" fill="#fff"/></svg></i>0 7000 5550</span>
    <span><i class="icon-dot"><svg width="8" height="8" viewBox="0 0 10 10"><path d="M2 1l2 2-1 1.5c.8 1.4 1.7 2.3 3 3L7.5 6l2 2-1.5 1.5C4.5 9 1 5.5.5 2z" fill="#fff"/></svg></i>CALL US 0400 555 019</span>
  </div>
  <nav class="main-nav abs">
    <span class="active">HOME</span><span>SHIPPING INFO</span><span>PRODUCTS</span><span>BEST SELLERS</span><span>CONTACT US</span>
  </nav>
</header>

<section class="hero abs" role="img" aria-label="Colourful party lights behind the slider"></section>
<div class="slider abs">
  <div class="crowd abs" role="img" aria-label="Silhouetted crowd with raised hands in green light"></div>
  <div class="slide-art abs" role="img" aria-label="Pile of glowing neon bracelets"></div>
  <div class="hero-title abs">ZIPPA THINGS</div>
  <div class="hero-sub abs">SCHOOLS AND FUNDRAISERS</div>
  <div class="hero-price abs"><small>Now</small><b>$8.99</b></div>
  <div class="hero-btn abs btn">SHOP NOW</div>
</div>

<h2 class="section-title abs">BEST SELLERS</h2>
<div class="section-rule abs"></div>
<div class="arrows abs">
  <span><svg width="6" height="6" viewBox="0 0 6 6"><path d="M4 0L1 3l3 3" stroke="#888" fill="none"/></svg></span>
  <span><svg width="6" height="6" viewBox="0 0 6 6"><path d="M2 0l3 3-3 3" stroke="#888" fill="none"/></svg></span>
</div>

<div class="products abs">
  <article class="card"><div class="card-art art-1" role="img" aria-label="Crossed glow sticks"></div>
    <div class="card-info"><div class="card-name">Duis aute irure dolor</div><div class="card-price">$200.00<span class="stars">★★★☆☆</span></div>
    <div class="cart"><svg width="10" height="10" viewBox="0 0 10 10"><path d="M0 1h2l1.5 5h5L10 3H3" stroke="#fff" fill="none"/><circle cx="4" cy="8.5" r="1" fill="#fff"/><circle cx="8" cy="8.5" r="1" fill="#fff"/></svg></div></div></article>
  <article class="card"><div class="card-art art-2" role="img" aria-label="Glowing bracelet rings"></div>
    <div class="card-info"><div class="card-name">Duis aute irure dolor</div><div class="card-price">$200.00<span class="stars">★★★☆☆</span></div>
    <div class="cart"><svg width="10" height="10" viewBox="0 0 10 10"><path d="M0 1h2l1.5 5h5L10 3H3" stroke="#fff" fill="none"/><circle cx="4" cy="8.5" r="1" fill="#fff"/><circle cx="8" cy="8.5" r="1" fill="#fff"/></svg></div></div></article>
  <article class="card"><div class="card-art art-3" role="img" aria-label="Bundle of glow sticks"></div>
    <div class="card-info"><div class="card-name">Duis aute irure dolor</div><div class="card-price">$200.00<span class="stars">★★★☆☆</span></div>
    <div class="cart"><svg width="10" height="10" viewBox="0 0 10 10"><path d="M0 1h2l1.5 5h5L10 3H3" stroke="#fff" fill="none"/><circle cx="4" cy="8.5" r="1" fill="#fff"/><circle cx="8" cy="8.5" r="1" fill="#fff"/></svg></div></div></article>
  <article class="card"><div class="card-art art-4" role="img" aria-label="Glowing ball made of linked sticks"></div>
    <div class="card-info"><div class="card-name">Duis aute irure dolor</div><div class="card-price">$200.00<span class="stars">★★★☆☆</span></div>
    <div class="cart"><svg width="10" height="10" viewBox="0 0 10 10"><path d="M0 1h2l1.5 5h5L10 3H3" stroke="#fff" fill="none"/><circle cx="4" cy="8.5" r="1" fill="#fff"/><circle cx="8" cy="8.5" r="1" fill="#fff"/></svg></div></div></article>
</div>

<div class="promo promo-left abs">
  <div class="promo-art abs" role="img" aria-label="Fan of coloured glow sticks"></div>
  <div class="promo-title abs">ZIPPA THINGS</div>
  <div class="btn-white abs">SHOP NOW</div>
</div>
<div class="promo promo-right abs" role="img" aria-label="Party crowd under coloured lights">
  <div class="promo-title abs">FREE DELIVERY</div>
  <div class="promo-sub abs">ON ALL ORDERS OVER $50</div>
  <div class="btn-white abs">SHOP NOW</div>
</div>

<div class="features abs">
  <div class="feature">
    <svg width="20" height="14" viewBox="0 0 18 12"><path d="M1 1h10v8H1zM11 4h4l2 3v2h-6" fill="none" stroke="#666"/><circle cx="4" cy="10" r="1.5" fill="#666"/><circle cx="14" cy="10" r="1.5" fill="#666"/></svg>
    <div><h4>FREE SHIPPING ONLY</h4><p>Free on all orders over fifty</p></div>
  </div>
  <div class="feature">
    <svg width="16" height="16" viewBox="0 0 14 14"><path d="M12 7a5 5 0 1 1-2-4M10 1v2.5H12.5" fill="none" stroke="#666"/></svg>
    <div><h4>14 DAYS FREE RETURNS</h4><p>Send items back within two weeks</p></div>
  </div>
  <div class="feature">
    <svg width="18" height="14" viewBox="0 0 16 12"><rect x="1" y="1" width="14" height="10" fill="none" stroke="#666"/><circle cx="8" cy="6" r="2" fill="none" stroke="#666"/></svg>
    <div><h4>CASH ON DELIVERY</h4><p>Pay when your order arrives</p></div>
  </div>
</div>

<footer class="site-footer abs"></footer>
<div class="foot-brand abs">ZIPPA things</div>
<div class="field field-name abs">Enter Name</div>
<div class="field field-email abs">Enter Email</div>
<div class="subscribe abs">SUBSCRIBE</div>

<div class="foot-col contact-col abs">
  <h5 class="accent">CONTACT US</h5>
  <ul>
    <li><svg width="7" height="9" viewBox="0 0 6 8"><path d="M3 0a3 3 0 0 1 3 3c0 2-3 5-3 5S0 5 0 3a3 3 0 0 1 3-3z" fill="#999"/></svg>Maple Creek, Northvale</li>
    <li><svg width="7" height="7" viewBox="0 0 10 10"><path d="M2 1l2 2-1 1.5c.8 1.4 1.7 2.3 3 3L7.5 6l2 2-1.5 1.5C4.5 9 1 5.5.5 2z" fill="#999"/></svg>Phone: (000) 555 0191</li>
    <li><svg width="8" height="6" viewBox="0 0 7 5"><rect width="7" height="5" fill="#999"/><path d="M0 0l3.5 3L7 0" stroke="#fff" fill="none" stroke-width=".6"/></svg>hello@zippathings.test</li>
  </ul>
</div>
<div class="socials abs"><span></span><span></span><span></span><span></span></div>

<div class="foot-col support-col abs">
  <h5>Customer Support</h5>
  <ul><li>Contact Us</li><li>Shipping &amp; Returns</li><li>Privacy Policy</li><li>Conditions of Use</li><li>My Account</li></ul>
</div>
<div class="foot-col account-col abs">
  <h5>My Account</h5>
  <ul><li>My Rewards</li><li>Register</li><li>Saved Rewards</li><li>Rewards FAQ</li><li>Rewards Terms</li><li>Sign In</li></ul>
</div>

<div class="bottom-bar abs">© 2016 ZIPPA things. All Rights Reserved.</div>
</body>
</html>
```